Quorvane - corporate Business Card

We need a good look and innovative business card for a new start up company based in Los Angeles called "Quorvane". We are in a payment business, including payment card, app, and ewallet. We are expert in online payment and Card not present (CNP) transaction.
We need an innovative, modern business card.

Our logo font is Aero Matics

Target Market(s)

Startup - Bank - Online Payment - Card Manufacturing

Industry/Entity Type

Startup

Contact Information for Business Card

phone: 424 555 0173 - Address: 4270 Marbrook blvd, Harlow Vale, CA 90417

Requirements
Must have
• Message: innovative, professional, expert, high tech, trust, online payment expert, security
Nice to have
• no comment
Should not have
• no Comment

```html
<!DOCTYPE html>
<html lang="en">
<head>
<meta charset="utf-8">
<title>Quorvane – Business Card</title>
<link href="https://fonts.googleapis.com/css2?family=Open+Sans:wght@400;600;700&display=swap" rel="stylesheet">
<style>
  :root {
    --bg: #2a2a2c;
    --brand-red: #b71f2e;
    --paper: #ffffff;
    --ink: #3a3a3a;
    --ink-soft: #555555;
    --rule: #d6d6d6;
  }
  * { margin: 0; padding: 0; box-sizing: border-box; }
  html, body {
    width: 1200px; height: 1000px; overflow: hidden;
    background: var(--bg);
    font-family: "Open Sans", Arial, sans-serif;
  }
  .stage { position: relative; width: 1200px; height: 1000px; }
  .card {
    position: absolute; left: 300px;
    width: 600px; height: 343px;
    border-radius: 22px;
    overflow: hidden;
  }
  /* Front */
  .card--front { top: 110px; background: var(--brand-red); }
  .brand {
    position: absolute; inset: 0;
    display: flex; align-items: center; justify-content: center; gap: 22px;
  }
  .brand__dot {
    width: 92px; height: 92px; border-radius: 50%;
    background: var(--paper);
  }
  .brand__name {
    color: var(--paper);
    font-weight: 600; font-size: 74px; letter-spacing: 1px;
    line-height: 1;
  }
  /* Back */
  .card--back { top: 520px; background: var(--brand-red); }
  .card__face {
    position: absolute; left: 0; top: 0; right: 0; height: 331px;
    background: var(--paper);
    border-radius: 22px 22px 18px 18px;
  }
  .identity {
    position: absolute; right: 340px; top: 142px; text-align: right;
  }
  .identity__name {
    font-weight: 700; font-size: 27px; color: var(--ink); letter-spacing: .3px;
    white-space: nowrap;
  }
  .identity__name .surname { color: var(--brand-red); }
  .identity__role { font-size: 17px; color: var(--ink); margin-top: -2px; }
  .divider {
    position: absolute; left: 290px; top: 120px;
    width: 1px; height: 96px; background: var(--rule);
  }
  .contact {
    position: absolute; left: 312px; top: 112px;
    font-size: 14.5px; color: var(--ink-soft); line-height: 1.3;
    white-space: nowrap;
  }
  .contact__address { margin-bottom: 10px; }
  .contact__list { list-style: none; }
  .contact__item { display: flex; align-items: center; gap: 12px; }
  .contact__icon { width: 11px; height: 11px; flex: none; }
  .contact__web .accent { color: var(--brand-red); }
</style>
</head>
<body>
<main class="stage">
  <section class="card card--front" aria-label="Card front">
    <div class="brand">
      <span class="brand__dot"></span>
      <span class="brand__name">quorvane</span>
    </div>
  </section>

  <section class="card card--back" aria-label="Card back">
    <div class="card__face">
      <div class="identity">
        <div class="identity__name">DORIAN <span class="surname">HALVEK</span></div>
        <div class="identity__role">Ceo &amp; Founder</div>
      </div>
      <div class="divider"></div>
      <div class="contact">
        <p class="contact__address">4270 Marbrook blvd,<br>Harlow Vale, CA 90417</p>
        <ul class="contact__list">
          <li class="contact__item">
            <svg class="contact__icon" viewBox="0 0 12 12" aria-hidden="true"><path fill="#b71f2e" d="M2.5 0.8 4.3 3.2 3.3 4.4c.7 1.6 2 2.9 3.6 3.6l1.2-1 2.4 1.8-.8 2.3C4.9 10.9 1 7.1.3 1.6z"/></svg>
            <span>424 555 0173</span>
          </li>
          <li class="contact__item">
            <svg class="contact__icon" viewBox="0 0 12 12" aria-hidden="true"><rect x="0.5" y="2" width="11" height="8" fill="#b71f2e"/><path d="M0.8 2.4 6 6.5l5.2-4.1" fill="none" stroke="#fff" stroke-width="1"/></svg>
            <span>yourname@email.com</span>
          </li>
          <li class="contact__item contact__web">
            <svg class="contact__icon" viewBox="0 0 12 12" aria-hidden="true"><circle cx="6" cy="6" r="5.5" fill="#b71f2e"/><path d="M0.5 6h11M6 .5c-2.4 3-2.4 8 0 11M6 .5c2.4 3 2.4 8 0 11" fill="none" stroke="#fff" stroke-width=".8"/></svg>
            <span>www.<span class="accent">websitename</span>.com</span>
          </li>
        </ul>
      </div>
    </div>
  </section>
</main>
</body>
</html>
```